Bright Ember Publicity is a new boutique Press Office with a small roster of well-chosen clients across an array of disciplines; from Art and Technology to Restaurants and Fashion. Based in Greenpoint Brooklyn, Bright Ember Publicity achieves outstanding results through hard work, tenacity, efficiency and a sense of humor. We need a simple, versatile and classic design. We would like each side of the card to be white text on a black background.

Boutique

```html
<!DOCTYPE html>
<html lang="en">
<head>
<meta charset="utf-8">
<title>Bright Ember Publicity – Business Card</title>
<link rel="stylesheet" href="https://fonts.googleapis.com/css2?family=Source+Sans+3:wght@400;600&display=swap">
<style>
  :root {
    --backdrop: #e9e7e5;
    --card-black: #050505;
    --card-panel: #151618;
    --ink-light: #ffffff;
    --shadow: rgba(0, 0, 0, 0.18);
  }
  * { box-sizing: border-box; margin: 0; padding: 0; }
  html, body {
    width: 1200px;
    height: 900px;
    overflow: hidden;
    background: var(--backdrop);
    font-family: "Source Sans 3", "Myriad Pro", sans-serif;
  }
  .canvas {
    position: relative;
    width: 1200px;
    height: 900px;
  }
  .card {
    position: absolute;
    width: 556px;
    height: 343px;
    background: var(--card-black);
    color: var(--ink-light);
    box-shadow: 0 6px 18px var(--shadow);
    overflow: hidden;
  }
  /* Front side */
  .card-front {
    left: 238px;
    top: 62px;
  }
  .front-panel {
    position: absolute;
    inset: 0;
    width: 100%;
    height: 100%;
  }
  .front-panel polygon { fill: var(--card-panel); }
  .holder {
    position: absolute;
    left: 35px;
    top: 30px;
    line-height: 1.3;
  }
  .holder-name { font-size: 18px; font-weight: 600; }
  .holder-role { font-size: 16px; font-weight: 400; }
  .front-brand {
    position: absolute;
    left: 35px;
    top: 130px;
    width: 260px;
    text-align: center;
  }
  .brand-name {
    font-family: "Source Sans 3", "Myriad Pro", sans-serif;
    font-weight: 400;
    text-transform: uppercase;
    letter-spacing: 0.22em;
    line-height: 1.35;
    color: var(--ink-light);
  }
  .front-brand .brand-name { font-size: 24px; }
  .contact-list {
    position: absolute;
    left: 35px;
    top: 246px;
    list-style: none;
    font-size: 16px;
    line-height: 21px;
  }
  .contact-list li { display: flex; align-items: center; gap: 6px; }
  .contact-list svg { width: 10px; height: 10px; fill: var(--ink-light); }
  .address {
    position: absolute;
    right: 30px;
    top: 270px;
    text-align: right;
    font-size: 15px;
    line-height: 21px;
    font-style: normal;
  }
  /* Back side */
  .card-back {
    left: 457px;
    top: 518px;
    width: 560px;
    display: flex;
    align-items: center;
    justify-content: center;
  }
  .back-brand { text-align: center; margin-top: 30px; }
  .back-brand .brand-name { font-size: 38px; }
</style>
</head>
<body>
<main class="canvas">
  <section class="card card-front" aria-label="Card front">
    <svg class="front-panel" viewBox="0 0 556 343" preserveAspectRatio="none" aria-hidden="true">
      <polygon points="442,0 556,0 556,343 220,343"/>
    </svg>
    <div class="holder">
      <p class="holder-name">Daniel Hartley</p>
      <p class="holder-role">Owner</p>
    </div>
    <div class="front-brand">
      <p class="brand-name">Bright Ember<br>Publicity</p>
    </div>
    <ul class="contact-list">
      <li>
        <svg viewBox="0 0 10 10" aria-hidden="true"><path d="M2.5 0h5a1 1 0 0 1 1 1v8a1 1 0 0 1-1 1h-5a1 1 0 0 1-1-1V1a1 1 0 0 1 1-1zm0 1.5v6h5v-6zm2.5 6.8a.5.5 0 1 0 0 1 .5.5 0 0 0 0-1z"/></svg>
        555-210-04817
      </li>
      <li>
        <svg viewBox="0 0 10 10" aria-hidden="true"><path d="M0 2h10v6H0zm1 .8v.3l4 2.5 4-2.5v-.3z"/></svg>
        hello@brightember.com
      </li>
      <li>
        <svg viewBox="0 0 10 10" aria-hidden="true"><circle cx="5" cy="5" r="5"/></svg>
        www.brightember.com
      </li>
    </ul>
    <address class="address">
      240 Franklin St Suite 310<br>
      Brooklyn, New York 11222
    </address>
  </section>

  <section class="card card-back" aria-label="Card back">
    <div class="back-brand">
      <p class="brand-name">Bright Ember<br>Publicity</p>
    </div>
  </section>
</main>
</body>
</html>
```